Private Mortgage Bank needs a brochure designed.

We need a brochure designed for a new Private Mortgage Bank based in Maryland. We provide financing options for real estate investors who are purchasing or refinancing an investment property. Our website is k7lendwise (dot) com. We are rental property specialists. I will attach our current logo and the business card design we have.
Target Market(s)
Real Estate Investors
Industry/Entity Type
Finance

```html
<!DOCTYPE html>
<html lang="en">
<head>
<meta charset="utf-8">
<title>K7 Lendwise Brochure</title>
<link href="https://fonts.googleapis.com/css2?family=Montserrat:wght@600;700;800&family=Open+Sans:ital,wght@0,400;0,600;0,700;1,600;1,700&display=swap" rel="stylesheet">
<style>
:root{
  --green:#5da52f;
  --green-dark:#2f7a1e;
  --green-light:#9ccc4a;
  --ink:#2b2b2b;
  --muted:#555;
  --paper:#ffffff;
  --bg:#eef0ee;
}
*{box-sizing:border-box;margin:0;padding:0}
html,body{width:747px;height:1200px;overflow:hidden;background:var(--bg);font-family:'Open Sans',sans-serif;color:var(--ink)}
.canvas{position:relative;width:747px;height:1200px}
.panel{position:absolute;background:var(--paper);overflow:hidden;box-shadow:0 2px 8px rgba(0,0,0,.12)}
.cover{left:249px;top:30px;width:249px;height:538px}
.spread{position:absolute;left:0;top:632px;width:747px;height:538px;display:flex;box-shadow:0 2px 10px rgba(0,0,0,.14);background:var(--paper);overflow:hidden}
.spread .col{position:relative;width:249px;height:538px;border-right:1px solid #eee}
.spread .col:last-child{border-right:none}
.photo{position:absolute;display:block}
.swoosh{position:absolute;left:0;width:100%}
/* cover */
.cover-photo{left:0;top:0;width:249px;height:205px;background:linear-gradient(160deg,#f4f3ee 0%,#e6e3da 55%,#e9c94a 78%,#d8d4c8 100%)}
.brand{position:absolute;left:0;right:0;top:250px;text-align:center}
.brand-mark{display:inline-flex;align-items:center;gap:7px}
.brand-dot{width:16px;height:16px;border-radius:50%;background:var(--green)}
.brand-name{font-family:'Montserrat',sans-serif;font-weight:700;font-size:15px;color:var(--green-dark);letter-spacing:.5px}
.brand-sub{font-size:6px;color:var(--muted);margin-top:4px;letter-spacing:.4px}
.cover-lede{position:absolute;left:26px;right:26px;top:310px;text-align:center;font-size:8.5px;line-height:1.5;font-weight:600;font-style:italic;color:var(--ink)}
.cover-foot{position:absolute;left:0;right:0;bottom:28px;text-align:center;color:#fff;font-size:6.5px;line-height:1.5;z-index:2}
.cover-foot strong{display:block;font-size:7.5px}
/* headers */
.tab{position:absolute;top:20px;height:20px;background:var(--green);color:#fff;font-family:'Montserrat',sans-serif;font-weight:700;font-size:8.5px;display:flex;align-items:center}
.tab-left{left:0;width:150px;padding-left:20px;border-radius:0 10px 10px 0}
.tab-right{right:0;width:160px;padding-left:14px;border-radius:10px 0 0 10px}
.hook{position:absolute;left:30px;right:16px;top:56px;font-weight:700;font-style:italic;color:var(--green);font-size:10px;line-height:1.3}
.steps{position:absolute;left:14px;right:14px;top:104px;list-style:none}
.step{margin-bottom:14px}
.step-head{display:flex;gap:7px;align-items:flex-start}
.box{flex:0 0 12px;height:12px;border:1.2px solid var(--green);margin-top:1px}
.step-title{font-size:7px;font-weight:700;line-height:1.3}
.step-title span{display:block;font-weight:400;color:var(--muted);font-size:6px}
.step p{font-size:6px;line-height:1.5;color:var(--muted);margin-top:6px}
/* middle */
.intro{position:absolute;left:18px;right:18px;top:16px;text-align:center;font-size:7.5px;line-height:1.5;font-weight:600;color:var(--green-dark)}
.intro p+p{margin-top:8px;color:var(--ink)}
.house-photo{left:0;top:110px;width:249px;height:160px;background:linear-gradient(180deg,#9cc7e8 0%,#cfe3f0 40%,#e8e6e0 62%,#7ea45a 100%)}
.quote{position:absolute;left:24px;right:20px;top:296px;font-size:8px;font-style:italic;font-weight:700;color:var(--green);line-height:1.45}
.quote-mark{position:absolute;left:-14px;top:-6px;font-size:22px;color:var(--green);font-family:'Montserrat',sans-serif}
.signoff{position:absolute;left:0;right:0;top:376px;text-align:center}
.signoff .name{font-family:'Montserrat',sans-serif;font-weight:700;font-size:10px}
.signoff .role{font-size:6.5px;color:var(--muted);line-height:1.5}
/* right */
.cs{position:absolute;left:16px;top:48px;font-size:7px;font-weight:700}
.philo{position:absolute;left:16px;right:16px;top:66px;font-size:6.5px;line-height:1.55;color:var(--muted)}
.checks{position:absolute;left:44px;top:150px;list-style:none}
.check{display:flex;gap:8px;align-items:flex-start;margin-bottom:10px}
.check .box{flex:0 0 11px;height:11px}
.check div{font-size:7px;font-weight:600;line-height:1.3}
.check span{display:block;font-size:6px;font-weight:400;color:var(--muted)}
.estate-photo{left:0;top:268px;width:249px;height:170px;background:linear-gradient(180deg,#a9cbe6 0%,#dbe8ef 45%,#f2f1ec 60%,#6f9a4a 100%)}
</style>
</head>
<body>
<div class="canvas">

  <section class="panel cover">
    <div class="photo cover-photo" role="img" aria-label="Bright living room with a yellow accent chair"></div>
    <svg class="swoosh" style="top:170px" width="249" height="70" viewBox="0 0 249 70">
      <path d="M0 38 C80 10 170 60 249 20 L249 0 C170 40 80 -5 0 25Z" fill="#fff"/>
      <path d="M0 40 C80 14 170 62 249 24 L249 34 C170 70 80 24 0 50Z" fill="var(--green)"/>
      <path d="M0 52 C80 28 170 72 249 38 L249 42 C170 76 80 34 0 56Z" fill="var(--green-light)"/>
    </svg>
    <div class="brand">
      <div class="brand-mark"><span class="brand-dot"></span><span class="brand-name">K7 LENDWISE, LLC</span></div>
      <div class="brand-sub">PRIVATE MORTGAGE BANK</div>
    </div>
    <p class="cover-lede">Our private mortgage is exclusively designed for financing investment properties.</p>
    <svg class="swoosh" style="bottom:0" width="249" height="110" viewBox="0 0 249 110">
      <path d="M0 40 C90 70 170 0 249 30 L249 110 L0 110Z" fill="var(--green)"/>
      <path d="M0 30 C90 62 170 -8 249 20 L249 26 C170 -2 90 68 0 36Z" fill="var(--green-light)"/>
    </svg>
    <div class="cover-foot"><strong>k7lendwise (dot) com</strong>Financing for rental property investors across Maryland.</div>
  </section>

  <section class="spread">
    <div class="col">
      <div class="tab tab-left">Start The Process</div>
      <p class="hook">Secure your Financing Before you go Shopping for a Property!</p>
      <ul class="steps">
        <li class="step">
          <div class="step-head"><span class="box"></span><div class="step-title">Complete Mortgage Application<span>Borrower Tools</span></div></div>
          <p>The mortgage application takes about ten minutes to complete. Submit it online and our team begins reviewing your file the same business day.</p>
        </li>
        <li class="step">
          <div class="step-head"><span class="box"></span><div class="step-title">Upload Bank Statements &amp; Photo ID<span>Borrower Tools</span></div></div>
          <p>Once your application is in, upload two recent bank statements and a clear photo ID through the secure portal to keep your file moving.</p>
        </li>
        <li class="step">
          <div class="step-head"><span class="box"></span><div class="step-title">Credit Report Review<span>Complete Tool</span></div></div>
          <p>We will run a soft credit check that does not affect your score, then send the results and next steps directly to your inbox.</p>
        </li>
      </ul>
      <svg class="swoosh" style="bottom:0" width="249" height="90" viewBox="0 0 249 90">
        <path d="M0 30 C90 70 170 10 249 40 L249 90 L0 90Z" fill="var(--green)"/>
        <path d="M0 20 C90 62 170 0 249 30 L249 36 C170 6 90 68 0 26Z" fill="var(--green-light)"/>
      </svg>
    </div>

    <div class="col">
      <div class="intro">
        <p>Our team will pre approve your mortgage application within 48 minutes of you providing the necessary and approved documents.</p>
        <p>Once you are pre approved you will receive a Proof of Funds Letter and Term Sheet.</p>
      </div>
      <div class="photo house-photo" role="img" aria-label="Modern two-storey white house with lawn"></div>
      <blockquote class="quote"><span class="quote-mark">&ldquo;</span>We have strategic relationships that give us access to financing options which are difficult for individuals to find.</blockquote>
      <div class="signoff">
        <div class="name">Dana Whitfield</div>
        <div class="role">K7 Commercial Mortgage<br>Founder | CEO</div>
      </div>
      <svg class="swoosh" style="bottom:0" width="249" height="80" viewBox="0 0 249 80">
        <path d="M0 40 C90 10 170 60 249 30 L249 80 L0 80Z" fill="var(--green)"/>
        <path d="M0 30 C90 0 170 52 249 20 L249 26 C170 58 90 6 0 36Z" fill="var(--green-light)"/>
      </svg>
    </div>

    <div class="col">
      <div class="tab tab-right">Underwriting Philosophy</div>
      <div class="cs">3 C's &ndash; Credit | Cash | Collateral</div>
      <p class="philo">We provide asset-based mortgage financing opportunities. We do not document the borrower's ability to repay the loan. Instead, we document the property's ability to become the loan through cash flow or appreciation.</p>
      <ul class="checks">
        <li class="check"><span class="box"></span><div>Credit<span>Soft Pull</span></div></li>
        <li class="check"><span class="box"></span><div>Cash Flow<span>Assets</span></div></li>
        <li class="check"><span class="box"></span><div>Collateral<span>Appraisal</span></div></li>
      </ul>
      <div class="photo estate-photo" role="img" aria-label="Large traditional house with porch and green lawn"></div>
      <svg class="swoosh" style="bottom:0" width="249" height="100" viewBox="0 0 249 100">
        <path d="M0 40 C80 70 170 10 249 45 L249 100 L0 100Z" fill="var(--green)"/>
        <path d="M0 30 C80 62 170 0 249 35 L249 41 C170 6 80 68 0 36Z" fill="var(--green-light)"/>
      </svg>
    </div>
  </section>

</div>
</body>
</html>
```